TKR Advisory Business Cards

Hi there,

I'd like to make a simple new business card design with the logo we already have created for our business.

I need a double sided business card with our logo on the front side and the company and person's details on the back side.

I'd like it to be on a white background and no background so I can potentially use it with either white paper or put it on different coloured paper in accordance with our business colours.

Please use the logo images I have attached and also the fonts.

So Front side:
- Logo in centre of business card (use medium logo so there is a pretty decent border around it, so don't want to fill the whole card but to make it prominent).

Back Side.
- We need 3 different business cards with the different people's name on each.

ie.

Dorian Halvreck
Business Development Manager

m +61 437 206 518
e dorian@tkradvisory.com.au
w tkradvisory.com.au

- Also I'd like to put only the cog/power button logo in the top right hand corner of the card.
(You might need to chop the current logo in half as I don't have a seperate log just for this)
- Also I'd like some lines running on the top left hand corner diagonally, anything that will add to the design or some swirling lines that add some cool effect to the card.

Also I'd like to maybe put our ABN in the bottom right hand corner of the card in a smaller font.

I'd like to also talk to the designer if possible so I can get my idea across a bit better.

Thanks!

Regards,
Dorian

```html
<!DOCTYPE html>
<html lang="en">
<head>
<meta charset="utf-8">
<title>TKR Advisory Business Cards</title>
<link rel="stylesheet" href="https://fonts.googleapis.com/css2?family=Fira+Sans+Condensed:ital,wght@0,400;0,700;1,300&display=swap">
<style>
  :root {
    --stage: #e9e7e4;
    --charcoal: #4a4a4c;
    --ink: #333335;
    --ink-soft: #555557;
    --orange: #f7941d;
    --orange-faint: rgba(247, 148, 29, 0.22);
    --line-grey: #b9b9bb;
    --paper: #ffffff;
  }
  * { box-sizing: border-box; margin: 0; padding: 0; }
  html, body {
    width: 1200px;
    height: 865px;
    overflow: hidden;
    background: var(--stage);
    font-family: "Fira Sans Condensed", "Arial Narrow", sans-serif;
  }
  .sheet {
    position: relative;
    width: 1200px;
    height: 865px;
  }
  .card {
    position: absolute;
    width: 560px;
    height: 320px;
    border-radius: 4px;
    overflow: hidden;
    background: var(--paper);
    box-shadow: 0 6px 18px rgba(0, 0, 0, 0.16);
  }
  .card-front   { left: 25px;  top: 82px; }
  .card-dorian  { left: 615px; top: 82px; }
  .card-marisol { left: 25px;  top: 442px; }
  .card-teodor  { left: 615px; top: 442px; }

  /* Front side */
  .card-front {
    display: flex;
    align-items: center;
    justify-content: center;
  }
  .brand {
    display: flex;
    align-items: center;
    gap: 14px;
  }
  .brand-dot {
    width: 50px;
    height: 50px;
    border-radius: 50%;
    background: var(--orange);
  }
  .brand-name {
    color: var(--orange);
    font-weight: 700;
    font-size: 50px;
    line-height: 1;
  }

  /* Back side */
  .side-band {
    position: absolute;
    left: 0;
    top: 0;
    width: 70px;
    height: 100%;
    background: var(--charcoal);
  }
  .corner-lines {
    position: absolute;
    left: 0;
    top: 0;
    width: 90px;
    height: 90px;
  }
  .corner-mark {
    position: absolute;
    right: 20px;
    top: 20px;
    width: 46px;
    height: 46px;
    border-radius: 50%;
    background: var(--orange);
  }
  .backdrop-mark {
    position: absolute;
    left: 300px;
    top: 70px;
    width: 210px;
    height: 210px;
    border-radius: 50%;
    background: var(--orange-faint);
  }
  .person {
    position: absolute;
    left: 92px;
    top: 24px;
  }
  .person-name {
    color: var(--ink);
    font-weight: 700;
    font-size: 22px;
    line-height: 1.1;
  }
  .person-role {
    color: var(--ink-soft);
    font-weight: 300;
    font-style: italic;
    font-size: 22px;
    line-height: 1.1;
  }
  .contact-list {
    position: absolute;
    right: 18px;
    bottom: 40px;
    list-style: none;
    display: flex;
    flex-direction: column;
    align-items: flex-end;
    gap: 6px;
  }
  .contact-item {
    display: flex;
    align-items: center;
    gap: 8px;
    color: var(--ink);
    font-weight: 700;
    font-size: 24px;
    line-height: 1;
  }
  .contact-icon {
    width: 30px;
    height: 30px;
    flex: none;
  }
  .abn {
    position: absolute;
    right: 20px;
    bottom: 13px;
    color: var(--ink-soft);
    font-weight: 400;
    font-size: 12px;
    letter-spacing: 0.4px;
  }
</style>
</head>
<body>
<svg width="0" height="0" style="position:absolute" aria-hidden="true">
  <defs>
    <symbol id="icon-phone" viewBox="0 0 38 38">
      <circle cx="19" cy="19" r="19" fill="#4a4a4c"/>
      <path d="M12 10.5c1-1 2.3-.9 3 .2l2 3c.5.8.3 1.8-.4 2.4l-1.3 1c.9 2.2 2.6 3.9 4.6 4.8l1-1.3c.6-.7 1.6-.9 2.4-.4l3 2c1.1.7 1.2 2 .2 3l-1.4 1.4c-1.4 1.4-4.8.6-8.6-3.2S9.2 13.3 10.6 11.9z" fill="#f7941d"/>
    </symbol>
    <symbol id="icon-mail" viewBox="0 0 38 38">
      <circle cx="19" cy="19" r="19" fill="#4a4a4c"/>
      <rect x="9.5" y="12.5" width="19" height="13" fill="none" stroke="#f7941d" stroke-width="2"/>
      <path d="M9.5 12.5 19 20l9.5-7.5M9.5 25.5l7-6M28.5 25.5l-7-6" fill="none" stroke="#f7941d" stroke-width="2"/>
    </symbol>
    <symbol id="icon-web" viewBox="0 0 38 38">
      <circle cx="19" cy="19" r="19" fill="#4a4a4c"/>
      <path d="M13 9l13 11.5-6 .6 3.6 6.8-2.6 1.4-3.6-6.9-4.4 4.2z" fill="#f7941d"/>
    </symbol>
    <symbol id="corner-lines" viewBox="0 0 90 90">
      <path d="M0 20 20 0" stroke="#f7941d" stroke-width="3"/>
      <path d="M0 34 34 0" stroke="#b9b9bb" stroke-width="2"/>
      <path d="M0 48 48 0" stroke="#f7941d" stroke-width="2"/>
      <path d="M0 62 62 0" stroke="#b9b9bb" stroke-width="1.5"/>
      <path d="M0 76 76 0" stroke="#f7941d" stroke-width="1"/>
    </symbol>
  </defs>
</svg>

<main class="sheet">

  <section class="card card-front" aria-label="Business card front">
    <div class="brand">
      <span class="brand-dot"></span>
      <span class="brand-name">TKR Advisory</span>
    </div>
  </section>

  <section class="card card-back card-dorian" aria-label="Business card back, Dorian Halvreck">
    <div class="side-band"></div>
    <svg class="corner-lines" aria-hidden="true"><use href="#corner-lines"/></svg>
    <span class="corner-mark"></span>
    <span class="backdrop-mark"></span>
    <div class="person">
      <p class="person-name">Dorian Halvreck</p>
      <p class="person-role">Business Development Manager</p>
    </div>
    <ul class="contact-list">
      <li class="contact-item"><span>+61 437 206 518</span><svg class="contact-icon" aria-hidden="true"><use href="#icon-phone"/></svg></li>
      <li class="contact-item"><span>dorian@tkradvisory.com.au</span><svg class="contact-icon" aria-hidden="true"><use href="#icon-mail"/></svg></li>
      <li class="contact-item"><span>tkradvisory.com.au</span><svg class="contact-icon" aria-hidden="true"><use href="#icon-web"/></svg></li>
    </ul>
    <p class="abn">ABN 52 418 903 276</p>
  </section>

  <section class="card card-back card-marisol" aria-label="Business card back, Marisol Quenby">
    <div class="side-band"></div>
    <svg class="corner-lines" aria-hidden="true"><use href="#corner-lines"/></svg>
    <span class="corner-mark"></span>
    <span class="backdrop-mark"></span>
    <div class="person">
      <p class="person-name">Marisol Quenby</p>
      <p class="person-role">Operations Director</p>
    </div>
    <ul class="contact-list">
      <li class="contact-item"><span>+61 412 958 304</span><svg class="contact-icon" aria-hidden="true"><use href="#icon-phone"/></svg></li>
      <li class="contact-item"><span>marisol@tkradvisory.com.au</span><svg class="contact-icon" aria-hidden="true"><use href="#icon-mail"/></svg></li>
      <li class="contact-item"><span>tkradvisory.com.au</span><svg class="contact-icon" aria-hidden="true"><use href="#icon-web"/></svg></li>
    </ul>
    <p class="abn">ABN 52 418 903 276</p>
  </section>

  <section class="card card-back card-teodor" aria-label="Business card back, Teodor Vasquel">
    <div class="side-band"></div>
    <svg class="corner-lines" aria-hidden="true"><use href="#corner-lines"/></svg>
    <span class="corner-mark"></span>
    <span class="backdrop-mark"></span>
    <div class="person">
      <p class="person-name">Teodor Vasquel</p>
      <p class="person-role">Senior Engineering Consultant</p>
    </div>
    <ul class="contact-list">
      <li class="contact-item"><span>+61 428 671 093</span><svg class="contact-icon" aria-hidden="true"><use href="#icon-phone"/></svg></li>
      <li class="contact-item"><span>teodor@tkradvisory.com.au</span><svg class="contact-icon" aria-hidden="true"><use href="#icon-mail"/></svg></li>
      <li class="contact-item"><span>tkradvisory.com.au</span><svg class="contact-icon" aria-hidden="true"><use href="#icon-web"/></svg></li>
    </ul>
    <p class="abn">ABN 52 418 903 276</p>
  </section>

</main>
</body>
</html>
```